Rebrand of 3 bottle labels for nail polish brand

The task is to make a rebranding of our current gel nail polish bottle design. We have become one of the leading european nail polish brand, so we want to improve the quality of the label design to a more scandinavian and minimalistic bottle design, which stille has to be recognisable and unique.

We have attached a more detailed description of the rebranding instructions for our gel polish bottles called "bottle task".
Updates

The Labels should not be just Black and White as stated. But should be mainly Black and White and then some of our color as explained in the uploaded file.

Target Market(s)

Girls and women age 18-55 Northern Europe

Industry/Entity Type

Cosmetic/ Nail Gel Polish

Colors

Designer to choose only greyscale colors for use in the design.

Requirements
Must have
• See attched design instruction
Nice to have
• Moderne, Minimalist, Recognizable and Unique look
Should not have
• Too many elements, too busy design

```html
<!DOCTYPE html>
<html lang="en">
<head>
<meta charset="utf-8">
<title>lumelle Base Coat Label</title>
<link href="https://fonts.googleapis.com/css2?family=Poppins:wght@300;400;500&display=swap" rel="stylesheet">
<style>
  :root {
    --backdrop: #e2e2e2;
    --label: #ffffff;
    --ink: #6f6f6f;
    --ink-soft: #9a9a9a;
    --rose: #c7a297;
    --rose-light: #e3cbc3;
  }
  * { margin: 0; padding: 0; box-sizing: border-box; }
  html, body {
    width: 1200px;
    height: 950px;
    overflow: hidden;
    background: var(--backdrop);
    font-family: "Poppins", sans-serif;
  }
  .canvas {
    width: 1200px;
    height: 950px;
    display: flex;
    align-items: center;
    justify-content: center;
  }
  .label {
    position: relative;
    width: 760px;
    height: 560px;
    background: var(--label);
    box-shadow: 0 18px 40px rgba(0,0,0,0.08);
    padding: 70px 80px;
    color: var(--ink);
  }
  .brand-name {
    font-size: 110px;
    font-weight: 400;
    letter-spacing: 2px;
    line-height: 1;
    color: var(--ink);
  }
  .product-type {
    margin-top: 26px;
    font-size: 34px;
    font-weight: 400;
    line-height: 1.15;
    color: var(--ink);
  }
  .product-method {
    font-size: 34px;
    font-weight: 400;
    line-height: 1.15;
    color: var(--ink);
  }
  .variant {
    position: relative;
    margin-top: 26px;
    width: 470px;
    height: 110px;
  }
  .variant-stroke {
    position: absolute;
    inset: 0;
    background: linear-gradient(100deg, var(--rose-light) 0%, var(--rose) 45%, var(--rose-light) 100%);
    opacity: 0.75;
  }
  .variant-band {
    position: absolute;
    left: 0;
    top: 32px;
    width: 420px;
    height: 46px;
    background: var(--label);
    display: flex;
    align-items: center;
    padding-left: 80px;
    font-size: 34px;
    font-weight: 500;
    letter-spacing: 1px;
    color: var(--rose);
  }
  .shade-number {
    position: absolute;
    right: 90px;
    top: 330px;
    width: 40px;
    height: 40px;
    border-radius: 50%;
    background: var(--rose);
    color: var(--label);
    font-size: 15px;
    font-weight: 500;
    display: flex;
    align-items: center;
    justify-content: center;
  }
  .volume {
    position: absolute;
    left: 80px;
    bottom: 60px;
    font-size: 30px;
    font-weight: 400;
    color: var(--rose);
  }
  .badge {
    position: absolute;
    right: 80px;
    bottom: 50px;
    width: 110px;
    height: 110px;
    border-radius: 50%;
    background: var(--rose);
  }
</style>
</head>
<body>
<main class="canvas">
  <section class="label">
    <h1 class="brand-name">lumelle</h1>
    <p class="product-type">Base Coat</p>
    <p class="product-method">SOAK OFF UV/LED</p>
    <div class="variant">
      <div class="variant-stroke" role="img" aria-label="Rose brush stroke texture behind the variant name"></div>
      <div class="variant-band">FLEXIBLE</div>
    </div>
    <span class="shade-number">01</span>
    <p class="volume">15ml ℮ 0.5oz</p>
    <span class="badge" aria-hidden="true"></span>
  </section>
</main>
</body>
</html>
```